Harborline Equipment Alliance Business Card Redesign

Logo has already been developed. The current business card is one sided. We'd like our mission on the back and more creativity so it pops. We may also like a tagline on the back
One call...all the service, all the savings. Examples are attached from our printer but we don't like them. The front is how we have our existing cards but the back is new. We are open to all ideas. We do like our colors/ brand of purple, black, white...

```html
<!DOCTYPE html>
<html lang="en">
<head>
<meta charset="utf-8">
<title>Harborline Equipment Alliance – Business Card</title>
<link href="https://fonts.googleapis.com/css2?family=Open+Sans:wght@400;600;700&family=Josefin+Sans:wght@400;600&display=swap" rel="stylesheet">
<style>
  :root {
    --purple: #7a3fb0;
    --purple-light: #9a74c4;
    --purple-deep: #6a3aa2;
    --charcoal: #2f2d33;
    --ink: #3c3a40;
    --grey: #6e6c72;
    --white: #ffffff;
    --paper: #f4f4f4;
    --backdrop: #2a2a2c;
  }
  * { box-sizing: border-box; margin: 0; padding: 0; }
  html, body { width: 1200px; height: 900px; overflow: hidden; }
  body {
    background: var(--backdrop);
    font-family: "Open Sans", Arial, sans-serif;
    position: relative;
  }
  .card {
    position: absolute;
    width: 560px;
    height: 320px;
    overflow: hidden;
    box-shadow: 0 14px 30px rgba(0,0,0,.45);
  }

  /* Back side */
  .card-back {
    left: 60px; top: 70px;
    background: linear-gradient(160deg, var(--purple-deep), var(--purple-light));
    color: var(--white);
    font-family: "Josefin Sans", "Century Gothic", sans-serif;
  }
  .mission { position: absolute; left: 34px; top: 40px; width: 230px; }
  .mission-title { font-weight: 600; font-size: 13px; letter-spacing: .5px; text-transform: uppercase; }
  .mission-text { font-size: 12.5px; line-height: 1.3; opacity: .85; margin-top: 2px; }
  .back-rule { position: absolute; left: 34px; top: 196px; width: 175px; height: 1px; background: rgba(255,255,255,.7); }
  .slogan {
    position: absolute; left: 34px; top: 222px;
    font-weight: 600; font-size: 17px; line-height: 1.25; text-transform: uppercase; letter-spacing: .5px;
  }
  .seal { position: absolute; left: 250px; top: -120px; width: 420px; height: 420px; }
  .seal-name {
    position: absolute; left: 318px; top: 60px; width: 220px;
    text-align: center; font-size: 28px; font-weight: 600; color: var(--white); line-height: 1.1;
  }

  /* Front side */
  .card-front {
    left: 580px; top: 470px;
    background: var(--paper);
    color: var(--ink);
  }
  .brand-mark { position: absolute; left: 34px; top: 70px; display: flex; align-items: center; gap: 10px; }
  .brand-dot { width: 16px; height: 16px; border-radius: 50%; background: var(--purple); }
  .brand-word { font-size: 22px; font-weight: 700; color: var(--charcoal); }
  .company { position: absolute; left: 250px; top: 52px; }
  .company-name { font-size: 17px; font-weight: 600; color: var(--purple); }
  .company-tagline { font-size: 13px; font-weight: 600; color: var(--charcoal); }
  .person { position: absolute; left: 34px; top: 218px; width: 176px; text-align: right; }
  .person-name { font-size: 15px; font-weight: 700; color: var(--grey); text-transform: uppercase; }
  .person-title { font-size: 12px; color: var(--grey); line-height: 1.3; }
  .divider { position: absolute; left: 222px; top: 212px; width: 1px; height: 70px; background: #c9c9c9; }
  .contact { position: absolute; left: 236px; top: 214px; font-size: 11.5px; line-height: 1.55; color: var(--ink); }
  .contact b { color: var(--purple); font-weight: 700; }
</style>
</head>
<body>

<section class="card card-back" aria-label="Card back">
  <div class="mission">
    <h2 class="mission-title">Our Mission</h2>
    <p class="mission-text">To keep every crew and job site running, safer, smarter, steadier while building lasting partner trust through the care and value we bring.</p>
  </div>
  <div class="back-rule"></div>
  <p class="slogan">One team –<br>every machine<br>every job site</p>
  <svg class="seal" viewBox="0 0 420 420" aria-hidden="true">
    <circle cx="210" cy="210" r="200" fill="var(--white)"/>
    <circle cx="210" cy="210" r="192" fill="var(--charcoal)"/>
  </svg>
  <p class="seal-name">Harborline Equipment Alliance</p>
</section>

<section class="card card-front" aria-label="Card front">
  <div class="brand-mark">
    <span class="brand-dot"></span>
    <span class="brand-word">Harborline</span>
  </div>
  <div class="company">
    <h1 class="company-name">Harborline Equipment Alliance</h1>
    <p class="company-tagline">Dependable Gear. Steady Support.</p>
  </div>
  <div class="person">
    <p class="person-name">Dana Whitfield</p>
    <p class="person-title">Business Development<br>Manager</p>
  </div>
  <div class="divider"></div>
  <div class="contact">
    <p>4180 Harbor View Drive, Suite 200, Tacoma, WA 98402</p>
    <p><b>M:</b> (555) 214-3080 · <b>F:</b> (555) 214-3081 · <b>C:</b> (555) 214-3099</p>
    <p><b>E:</b> dwhitfield@HarborlineAlliance.com</p>
  </div>
</section>

</body>
</html>
```